Attention Getting Doorhanger Postcard Campaign offering HUGE Rebate on New Construction Homes

I am reestablishing my real estate career in the far North Dallas, TX area and want to offer a rebate on new construction homes to help get me started. I am requesting a doorhanger as my first project but would like a theme that I can carry over to other projects including postcards and other marketing items. I want it to look high end, clean, professional and classy. I am attaching a copy of a flier that I created that needs (no graphic designer here) some prettying up. But this is just to give you an idea of the type of style that is of interest to me.

Target Market(s)

Home buyers for new construction in far north dallas suburbs. Usually a move up buyer.

Industry/Entity Type

Real Estate

Colors

Designer to choose colors to be used in the design.

Requirements
Must have
• Catch phrase, draw attention, classy clean lines, current trend colors of blues and grays. My information, Marston Pryce logo, equal housing and realtor logos. Fine Print: Not intended to solicit homes already listed for sale or buyers already in a buyers agency agreement with another brokerage. Please include offer details as listed in my flier. Again I am interested in a door hanger and the next round would be a flier or postcard.
Nice to have
• Picture of new homes that are in line with what is being built in my area. A few home builders sites: Coastal Beacon, Riverbend Homes, Fenwick Homes, Calloway Homes.

```html
<!DOCTYPE html>
<html lang="en">
<head>
<meta charset="utf-8">
<title>New Construction Rebate Door Hanger</title>
<link href="https://fonts.googleapis.com/css2?family=Roboto+Condensed:wght@300;400;700;900&family=Roboto:wght@400;700&display=swap" rel="stylesheet">
<style>
  :root{
    --backdrop:#939598;
    --slate:#58595b;
    --brand-blue:#0a5cb8;
    --ink:#3a3a3c;
    --soft-ink:#5b5b5e;
    --paper:#ffffff;
    --dot:#6d6e71;
    --broker-red:#b40101;
  }
  *{box-sizing:border-box;margin:0;padding:0}
  html,body{width:1200px;height:2601px;overflow:hidden;background:var(--backdrop)}
  body{position:relative;font-family:"Roboto Condensed",Arial,sans-serif;color:var(--ink)}
  .hanger{position:absolute;left:165px;top:90px;width:875px;height:2419px;background:var(--paper);overflow:hidden}
  .hanger-top{position:absolute;left:0;top:0;width:875px;height:1124px;
    background:linear-gradient(180deg,var(--slate) 0%,var(--slate) 55%,#6f6a66 72%,#8d7d6a 100%)}
  .hole-guide{position:absolute;left:0;top:0;z-index:2}
  .home-photo{position:absolute;left:0;top:600px;width:875px;height:524px;
    background:linear-gradient(180deg,rgba(88,89,91,0) 0%,#7d7166 30%,#8a7660 55%,#6b6a55 78%,#8d8a84 100%)}
  .headline{position:absolute;left:0;top:975px;width:875px;height:150px;color:var(--paper);font-weight:900;line-height:1;z-index:2}
  .headline .awe{position:absolute;left:86px;top:0;font-size:94px;letter-spacing:2px}
  .headline .and-then{position:absolute;left:287px;top:4px;font-family:"Roboto",sans-serif;font-weight:400;font-size:32px}
  .headline .some{position:absolute;left:425px;top:41px;font-size:94px;letter-spacing:2px}
  .offer-band{position:absolute;left:0;top:1124px;width:875px;height:107px;background:var(--brand-blue);color:var(--paper);
    padding:24px 0 0 40px;font-size:34px;line-height:42px}
  .offer-band strong{font-weight:700;font-size:40px}
  .offer-band b{font-weight:700}
  .benefits{position:absolute;left:40px;top:1258px;width:805px;list-style:none;font-size:29px;line-height:37px;color:var(--soft-ink)}
  .benefits li{position:relative;padding-left:28px;margin-bottom:17px;text-align:justify}
  .benefits li::before{content:"";position:absolute;left:0;top:13px;width:15px;height:15px;border-radius:50%;background:var(--brand-blue)}
  .savings{position:absolute;left:40px;top:1640px;width:783px;height:140px}
  .savings svg{position:absolute;left:0;top:0}
  .example{position:absolute;left:16px;top:10px;color:var(--paper);font-size:25px;line-height:29px}
  .example h3{font-size:33px;font-weight:700;line-height:36px;margin-bottom:4px}
  .example b{font-size:29px}
  .example small{display:block;font-size:17px;line-height:20px}
  .maximize{position:absolute;left:440px;top:10px;width:340px;color:var(--paper);font-size:25px;line-height:28px}
  .maximize h3{font-size:31px;font-weight:700;line-height:34px}
  .maximize b{font-weight:700}
  .process{position:absolute;left:0;top:1790px;width:875px;height:235px}
  .process svg{position:absolute;left:0;top:0}
  .process h3{position:absolute;left:40px;top:6px;font-size:33px;font-weight:700;color:var(--brand-blue)}
  .process .step{position:absolute;font-size:24px;line-height:27px;color:var(--ink)}
  .process .step b{font-weight:700}
  .agent{position:absolute;left:0;top:2029px;width:875px;height:291px;background:var(--brand-blue);color:var(--paper)}
  .agent .intro{position:absolute;left:40px;top:20px;width:700px;font-size:24px;line-height:29px;font-weight:300}
  .agent .intro b{font-weight:700}
  .agent .name{position:absolute;left:38px;top:100px;font-size:76px;font-weight:400;line-height:1}
  .agent .creds{position:absolute;left:40px;top:195px;font-size:25px}
  .agent .contact{position:absolute;left:40px;top:228px;font-size:25px;font-weight:700}
  .agent-portrait{position:absolute;left:770px;top:22px;width:98px;height:217px;
    background:linear-gradient(180deg,#6b4a3a 0%,#a3725a 45%,#2f2c33 100%)}
  .footer{position:absolute;left:0;top:2320px;width:875px;height:99px;background:var(--paper)}
  .brokerage{position:absolute;left:35px;top:30px;font-family:"Roboto",sans-serif;font-weight:700;font-size:24px;color:var(--broker-red);display:flex;align-items:center;gap:9px}
  .brokerage .mark{width:16px;height:16px;background:var(--broker-red)}
  .fine-print{position:absolute;left:285px;top:6px;width:570px;font-size:14px;line-height:16px;color:var(--soft-ink)}
  .independent{position:absolute;left:285px;top:64px;font-size:23px;font-weight:700;color:var(--brand-blue)}
</style>
</head>
<body>
<main class="hanger">
  <section class="hanger-top">
    <div class="home-photo" role="img" aria-label="Brick and stone two-story new construction home at dusk with lit windows and landscaped front walk"></div>
    <svg class="hole-guide" width="875" height="620" viewBox="0 0 875 620" aria-hidden="true">
      <circle cx="437" cy="390" r="200" fill="none" stroke="#ffffff" stroke-width="3" stroke-dasharray="20 12"/>
      <circle cx="437" cy="390" r="113" fill="#ffffff"/>
    </svg>
    <h1 class="headline">
      <span class="awe">AWE</span><span class="and-then">and then</span><span class="some">SOME</span>
    </h1>
  </section>

  <p class="offer-band">receive A minimum of <strong>2.5%</strong> or more to put towards<br>your <b>NEW CONSTRUCTION</b> home!</p>

  <ul class="benefits">
    <li>We work with 100's of builders in the local area so you are not limited to a few "select" builders.</li>
    <li>Home builders have the same bottom line sales price whether you have a REALTOR® representing you or not.</li>
    <li>Rebate program will not affect the price you pay for your home. Brokerage fees are paid through a separate marketing fund, not from the sales price of your home.</li>
    <li>Rebate program is in ADDITION to any builder or lender incentives.</li>
  </ul>

  <section class="savings">
    <svg width="783" height="140" viewBox="0 0 783 140" aria-hidden="true">
      <polygon points="0,0 420,0 400,140 0,140" fill="var(--brand-blue)"/>
      <polygon points="432,0 783,0 783,140 412,140" fill="var(--brand-blue)"/>
    </svg>
    <div class="example">
      <h3>For Example:</h3>
      <p><b>$400,000</b> equals a <b>$10,000</b> rebate!</p>
      <p><b>$500,000</b> equals a <b>$12,500</b> rebate!</p>
      <small>*Lender approval required.</small>
    </div>
    <div class="maximize">
      <h3>Maximize Your Savings!</h3>
      <p>My <b>Buy &amp; List package offers a FLAT FEE on the sale of your current home. Saving you</b></p>
    </div>
  </section>

  <section class="process">
    <h3>How it works:</h3>
    <svg width="875" height="235" viewBox="0 0 875 235" aria-hidden="true">
      <path d="M40 178 C130 140 220 150 282 150 C360 150 390 105 473 112 C560 120 600 150 659 140 C720 130 760 95 820 82" fill="none" stroke="var(--brand-blue)" stroke-width="7" stroke-linecap="round"/>
      <circle cx="282" cy="150" r="15" fill="var(--dot)"/>
      <circle cx="473" cy="112" r="15" fill="var(--dot)"/>
      <circle cx="659" cy="140" r="15" fill="var(--dot)"/>
      <circle cx="820" cy="82" r="15" fill="var(--dot)"/>
    </svg>
    <p class="step" style="left:220px;top:56px;text-align:right">Contact Lauren<br>to register</p>
    <p class="step" style="left:408px;top:14px">Find your<br>New Home</p>
    <p class="step" style="left:704px;top:14px;text-align:right">Close &amp; Receive<br>your <b>REBATE!</b></p>
    <p class="step" style="left:607px;top:172px">Sign your Contract</p>
  </section>

  <section class="agent">
    <p class="intro">I've sold hundreds of homes in the North Dallas area over the last 13 years, specializing in new construction homes. I would love to help you make your new home dreams a reality. <b>Lauren</b></p>
    <h2 class="name">Lauren Ashby</h2>
    <p class="creds">REALTOR®, CRS, ABR, CNHS, CHMS</p>
    <p class="contact">Mobile: 469.555.0187 | Email: laurenashby@example.com</p>
    <div class="agent-portrait" role="img" aria-label="Portrait of the agent"></div>
  </section>

  <footer class="footer">
    <p class="brokerage"><span class="mark"></span>Marston Pryce</p>
    <p class="fine-print">Not intended to solicit clients in a buyer agency agreement with other brokers or for properties that may already be listed for sale. Lender authorization required for rebates. Rebates do not apply on the purchase of a preowned home.</p>
    <p class="independent">Each Office Is Independently Owned &amp; Operated</p>
  </footer>
</main>
</body>
</html>
```